Need UI Design for HRIS/Company Employee Portal

Currently have a custom built system that we hire and use as our employee database and employee portal for everyone in our company. The software has evolved dramatically and needs to be completely user friendly and aesthetically pleasing. Attached are a few ideas and pages we already have. Please make 5 designs for the 5 different pages below. Would need all specifications of content used, color code, font/typography, icons used, etc. We can pretty much pull any information from anywhere we have for example, employee photo, address, DOB, Hire date, Title, ETC.

-Company Staff/Admin Welcome Page
- We want quick shortcuts/buttons or icons for staff functions, such as terminate, hire, information change, reports, etc
-Employee Profile Welcome Page
- We want quick shortcuts/buttons or icons for direct deposit, time off request, information change, pay stubs
-List of Applications/Candidates Page
-Profile Search Page
-Manage Inventory

Target Market(s)

Employees

Industry/Entity Type

It Company

Coding

Coded - Design and coding required

Number of Pages Required

5+ page

Font styles to use
Sans Serif

Requirements
Must have
• Must be professional! Aesthetics, Icons, Easy User Interface, Modern New technology look, can be responsive to mobile
Should not have
• Nothing old school

```html
<!DOCTYPE html>
<html lang="en">
<head>
<meta charset="utf-8">
<title>Employee Portal – Home</title>
<link href="https://fonts.googleapis.com/css2?family=Lato:ital,wght@0,400;0,700;1,400&display=swap" rel="stylesheet">
<style>
:root{
  --blue:#2a5d9f;
  --blue-dark:#1f4a82;
  --yellow:#f3d34a;
  --footer:#f0da6a;
  --page:#f3f3f3;
  --panel:#ffffff;
  --strip:#e6e6e6;
  --line:#e3e3e3;
  --text:#222;
  --muted:#5d6873;
  --soft:#f1f2f4;
}
*{box-sizing:border-box;margin:0;padding:0}
html,body{width:1200px;height:1043px;overflow:hidden}
body{font-family:'Lato',sans-serif;background:var(--page);color:var(--text);position:relative}

/* header */
.topbar{position:absolute;left:0;top:0;width:1200px;height:85px;background:#fff;box-shadow:0 1px 3px rgba(0,0,0,.08)}
.brand{position:absolute;left:43px;top:30px;display:flex;align-items:center;gap:8px;font-size:14px;font-weight:700;color:var(--blue)}
.brand-mark{width:22px;height:22px;border-radius:50%;background:var(--blue)}
.search{position:absolute;left:314px;top:19px;width:556px;height:42px;border:1px solid #cfcfcf;background:#fff}
.search svg{position:absolute;left:9px;top:9px}
.tool{position:absolute;top:25px;width:30px;height:30px;background:#eee;border-radius:2px;display:flex;align-items:center;justify-content:center}
.tool .count{position:absolute;top:-7px;right:-5px;width:16px;height:16px;border-radius:50%;color:#fff;font-size:10px;font-weight:700;display:flex;align-items:center;justify-content:center}
.sep{position:absolute;top:25px;width:1px;height:28px;background:#ddd}
.user{position:absolute;left:1070px;top:0;width:87px;height:85px;background:#eeeeee;text-align:center;font-size:13px;color:var(--muted)}
.user .avatar{width:42px;height:42px;border-radius:50%;margin:11px auto 4px;background:linear-gradient(135deg,#8f96a0,#3c434c)}

/* sidebar */
.sidebar{position:absolute;left:43px;top:85px;width:254px;height:912px;background:#fff}
.sidebar .band{height:73px;background:#e6e6e6}
.photo{position:absolute;left:57px;top:32px;width:140px;height:140px;border-radius:50%;border:5px solid #fff;box-shadow:0 0 0 1px #e6e6e6;background:linear-gradient(160deg,#c9d6e0,#8ea3b3 60%,#6c7f8e)}
.status{position:absolute;top:190px;left:0;width:254px;text-align:center;font-size:13.5px;line-height:19px}
.status h2{font-size:17px;font-weight:700;margin-bottom:4px}
.status-rule{position:absolute;left:39px;top:228px;width:1px;height:40px;background:var(--line)}
.contact{position:absolute;left:0;top:267px;width:254px;list-style:none}
.contact li{display:flex;border-top:1px solid var(--line);font-size:13px;color:#333;line-height:17px}
.contact .ico{width:39px;flex:none;border-right:1px solid var(--line);display:flex;justify-content:center;padding-top:12px}
.contact .val{padding:12px 10px}
.details{position:absolute;left:13px;top:587px;width:227px;height:299px;background:var(--soft);border-radius:4px;padding:6px 0;font-size:13px}
.details dl{display:grid;grid-template-columns:130px 1fr;row-gap:0}
.details dt{height:36.5px;display:flex;align-items:center;padding-left:7px;color:#333;position:relative}
.details dt::after{content:":";position:absolute;right:4px;top:7px;font-size:11px}
.details dt.last::after{content:""}
.details dd{height:36.5px;display:flex;align-items:center;font-weight:700;color:#222}

/* nav */
.mainnav{position:absolute;left:313px;top:110px;display:flex;font-size:14.5px;font-weight:700;color:var(--muted)}
.mainnav a{color:inherit;text-decoration:none;padding:0 19px;border-left:1px solid #d6d6d6;line-height:22px}
.mainnav a:first-child{padding-left:0;border-left:0;color:#4a525c;position:relative}
.mainnav a:first-child::after{content:"";position:absolute;left:0;bottom:-7px;width:38px;height:2px;background:var(--yellow)}
.mainnav a:last-child{padding-right:0}

/* tiles */
.tiles{position:absolute;left:313px;top:163px;display:grid;grid-template-columns:273px 273px 273px;column-gap:10px;row-gap:17px}
.tile{height:105px;background:#fff;position:relative;display:flex;align-items:center;box-shadow:0 1px 2px rgba(0,0,0,.08)}
.tile::before{content:"";position:absolute;left:0;top:0;width:54px;height:100%;background:var(--strip)}
.tile .badge{position:relative;margin-left:20px;width:70px;height:70px;border-radius:50%;background:var(--blue);border:3px solid #fff;box-shadow:0 0 0 1px #ddd;display:flex;align-items:center;justify-content:center}
.tile .label{margin-left:14px;font-size:20px;line-height:19px;color:var(--muted)}

/* messages */
.message{position:absolute;top:563px;width:273px;height:255px;background:#fff;box-shadow:0 1px 2px rgba(0,0,0,.08)}
.message header{height:39px;background:#e4e4e4;display:flex;align-items:center;padding-left:8px;font-size:18px;font-weight:700;color:#4a525c;gap:9px}
.message header .chip{width:30px;height:28px;background:var(--blue);display:flex;align-items:center;justify-content:center}
.message blockquote{padding:20px 20px 0 20px;font-style:italic;font-size:14px;line-height:22px;color:#333;letter-spacing:.3px}
.message .q{font-size:40px;line-height:0;color:#c5c5c5;font-style:normal;font-weight:700;vertical-align:-12px}
.crest{position:absolute;left:916px;top:562px;width:205px;height:242px}

/* footer */
.footer{position:absolute;left:0;top:997px;width:1200px;height:46px;background:var(--footer);text-align:center;font-size:13.5px;line-height:46px;color:#333}
</style>
</head>
<body>

<header class="topbar">
  <div class="brand"><span class="brand-mark"></span>Sentinel Watch Services</div>
  <div class="search">
    <svg width="26" height="26" viewBox="0 0 26 26" fill="none" stroke="#c8c8c8" stroke-width="3.5"><circle cx="11" cy="11" r="8"/><path d="M17 17l6 6" stroke-linecap="round"/></svg>
  </div>
  <div class="tool" style="left:904px">
    <svg width="18" height="13" viewBox="0 0 18 13" fill="none" stroke="#c3c3c3" stroke-width="1.5"><rect x="1" y="1" width="16" height="11"/><path d="M1 1l8 6 8-6"/></svg>
    <span class="count" style="background:var(--blue)">5</span>
  </div>
  <div class="sep" style="left:948px"></div>
  <div class="tool" style="left:964px">
    <svg width="16" height="18" viewBox="0 0 16 18" fill="#c3c3c3"><path d="M8 1c3 0 5 2 5 5v5l2 3H1l2-3V6c0-3 2-5 5-5z"/><circle cx="8" cy="16" r="2"/></svg>
    <span class="count" style="background:#111">2</span>
  </div>
  <div class="sep" style="left:1008px"></div>
  <div class="tool" style="left:1021px">
    <svg width="18" height="18" viewBox="0 0 18 18" fill="none" stroke="#c3c3c3" stroke-width="2" stroke-linecap="round"><path d="M5 4a7 7 0 1 0 8 0"/><path d="M9 1v7"/></svg>
  </div>
  <div class="user"><div class="avatar" role="img" aria-label="Profile photo of the signed-in user"></div>Dale Marsh</div>
</header>

<aside class="sidebar">
  <div class="band"></div>
  <div class="photo" role="img" aria-label="Employee profile photo"></div>
  <div class="status">
    <h2>Status</h2>
    <p>Hire date 8/1/2000</p>
    <p>17 years</p>
  </div>
  <div class="status-rule"></div>
  <ul class="contact">
    <li style="height:36px"><span class="ico"><svg width="16" height="15" viewBox="0 0 16 15" fill="var(--blue)"><circle cx="8" cy="4" r="3.5"/><path d="M1 15c0-4 3-6 7-6s7 2 7 6z"/></svg></span><span class="val">Marcus Ellery</span></li>
    <li style="height:87px"><span class="ico"><svg width="12" height="16" viewBox="0 0 12 16" fill="var(--blue)"><path d="M6 0a6 6 0 0 1 6 6c0 4-6 10-6 10S0 10 0 6a6 6 0 0 1 6-6zm0 3.5a2.5 2.5 0 1 0 0 5 2.5 2.5 0 0 0 0-5z"/></svg></span><span class="val" style="padding-top:7px">Lorem ipsum dolor sit amet,<br>sectetuer adipiscing<br>20165</span></li>
    <li style="height:38px"><span class="ico"><svg width="16" height="16" viewBox="0 0 16 16" fill="var(--blue)"><rect x="7" y="0" width="2" height="16"/><path d="M1 3h12l2 2-2 2H1zM3 9h12v4H3L1 11z"/></svg></span><span class="val" style="padding-top:11px">Consectetuer elit</span></li>
    <li style="height:38px"><span class="ico"><svg width="20" height="16" viewBox="0 0 20 16" fill="none" stroke="var(--blue)" stroke-width="1.8"><path d="M1 7l9-6 9 6v8H1z"/><path d="M1 7l9 6 9-6"/></svg></span><span class="val" style="padding-top:11px">elit20165</span></li>
    <li style="height:38px"><span class="ico"><svg width="12" height="18" viewBox="0 0 12 18" fill="none" stroke="var(--blue)" stroke-width="2"><rect x="1" y="1" width="10" height="16" rx="2"/><path d="M4 14h4"/></svg></span><span class="val" style="padding-top:11px">055 501 7342</span></li>
    <li style="height:38px"><span class="ico"><svg width="17" height="17" viewBox="0 0 17 17" fill="var(--blue)"><path d="M3 0l3 4-2 2c1 3 4 6 7 7l2-2 4 3-2 3C8 17 0 9 0 3z"/></svg></span><span class="val" style="padding-top:11px">5550148823</span></li>
    <li style="height:38px;border-bottom:1px solid var(--line)"><span class="ico"><svg width="20" height="13" viewBox="0 0 20 13" fill="var(--blue)"><path d="M0 0h20v13H0z"/><path d="M1 1l9 7 9-7" fill="none" stroke="#fff" stroke-width="1.6"/></svg></span><span class="val" style="padding-top:11px">info@example.com</span></li>
  </ul>
  <div class="details">
    <dl>
      <dt>DOB</dt><dd>3/12/1986</dd>
      <dt>Guard Card Number</dt><dd>skod145DS4</dd>
      <dt>Guard Card Expiry</dt><dd>8/1/2030</dd>
      <dt>SSN</dt><dd>1688</dd>
      <dt>Twic Card Number</dt><dd>2683268</dd>
      <dt>ID Document Type</dt><dd>sd2498335</dd>
      <dt>ID Document Expiry</dt><dd>1686ad833</dd>
      <dt class="last">Report To</dt><dd>Phoenix, AZ</dd>
    </dl>
  </div>
</aside>

<nav class="mainnav">
  <a href="#">Home</a><a href="#">Personal Licenses</a><a href="#">Forms\ Requests</a><a href="#">Team Contacts</a><a href="#">Benifits</a><a href="#">Training</a><a href="#">Equipment</a><a href="#">Help</a>
</nav>

<section class="tiles">
  <div class="tile"><span class="badge"><svg width="30" height="34" viewBox="0 0 30 34" fill="none" stroke="var(--yellow)" stroke-width="2.2"><rect x="6" y="2" width="20" height="26" rx="2"/><path d="M4 6v26h18"/><path d="M11 10h10M11 15h10M11 20h10"/></svg></span><span class="label">Documents</span></div>
  <div class="tile"><span class="badge"><svg width="30" height="36" viewBox="0 0 30 36" fill="none" stroke="var(--yellow)" stroke-width="2.2"><rect x="3" y="2" width="24" height="30" rx="2"/><path d="M9 9h12M9 14h12"/><circle cx="11" cy="23" r="4"/><path d="M9 27l-1 6 3-2 3 2-1-6"/></svg></span><span class="label">Licenses</span></div>
  <div class="tile"><span class="badge"><svg width="34" height="30" viewBox="0 0 34 30" fill="none" stroke="var(--yellow)" stroke-width="3.4" stroke-linecap="round"><path d="M22 6A12 12 0 1 0 22 24"/><path d="M12 15h20M26 9l6 6-6 6"/></svg></span><span class="label">Terminate</span></div>

  <div class="tile"><span class="badge"><svg width="20" height="38" viewBox="0 0 20 38" fill="var(--yellow)"><circle cx="12" cy="5" r="4.5"/><path d="M5 14h10l-4 16c0 2 1 2 5 0l-1 3c-5 4-12 5-10-2l3-12H5z"/></svg></span><span class="label">Information<br>Change</span></div>
  <div class="tile"><span class="badge"><svg width="34" height="32" viewBox="0 0 34 32" fill="none" stroke="var(--yellow)" stroke-width="2.2"><rect x="2" y="16" width="30" height="14" rx="2"/><path d="M2 22h30"/><path d="M10 16l6-12 10 5-3 7"/><circle cx="17" cy="10" r="2"/></svg></span><span class="label">Direct<br>Deposit</span></div>
  <div class="tile"><span class="badge"><svg width="36" height="34" viewBox="0 0 36 34" fill="none" stroke="var(--yellow)" stroke-width="3" stroke-linecap="round"><path d="M6 17A14 14 0 1 1 10 27"/><path d="M2 13l4 5 5-4"/><path d="M20 9v9l6 4"/></svg></span><span class="label">Time Off<br>Request</span></div>

  <div class="tile"><span class="badge"><svg width="36" height="30" viewBox="0 0 36 30" fill="none" stroke="var(--yellow)" stroke-width="2.2"><rect x="2" y="10" width="30" height="18" rx="2"/><path d="M7 17h10M7 22h8"/><path d="M22 22l10-20" stroke-width="3"/><circle cx="26" cy="21" r="3"/></svg></span><span class="label">Paystubs</span></div>
  <div class="tile"><span class="badge"><svg width="32" height="26" viewBox="0 0 32 26"><path d="M11 5V2h10v3" fill="none" stroke="var(--yellow)" stroke-width="2.4"/><rect x="1" y="5" width="30" height="20" rx="3" fill="var(--yellow)"/><circle cx="16" cy="15" r="6" fill="var(--blue)"/><path d="M16 11v8M12 15h8" stroke="var(--yellow)" stroke-width="2.2"/></svg></span><span class="label">Health<br>Insurance</span></div>
  <div class="tile"><span class="badge"><svg width="36" height="36" viewBox="0 0 36 36" fill="none" stroke="var(--yellow)" stroke-width="3"><circle cx="15" cy="15" r="8"/><path d="M15 2v5M15 23v5M2 15h5M23 15h5M6 6l3 3M21 21l3 3M24 6l-3 3M6 24l3-3"/><path d="M20 20l12 12" stroke-width="4" stroke-linecap="round"/></svg></span><span class="label">Equipment /<br>Uniform</span></div>
</section>

<article class="message" style="left:313px">
  <header><span class="chip"><svg width="20" height="18" viewBox="0 0 20 18" fill="var(--yellow)"><path d="M1 1h11v8H6l-3 3V9H1z"/><path d="M8 11h5l3 3v-3h3V4h-5v7z" opacity=".85"/></svg></span>Emloyess Secial Message</header>
  <blockquote><span class="q">&ldquo;</span> Lorem ipsum dolor amet, conse ctetuer adipiscing elit, sed diam nonu mmy nibh euis mod tincidunt ut laore et dolore ma gna aliquam erat volutpat. Ut wisi enim ad ,  Lorem ipsum dolor amet, conse ctetuer adipiscing elit, sed diam nonummy. <span class="q">&rdquo;</span></blockquote>
</article>
<article class="message" style="left:599px">
  <header><span class="chip"><svg width="20" height="18" viewBox="0 0 20 18" fill="var(--yellow)"><path d="M1 1h11v8H6l-3 3V9H1z"/><path d="M8 11h5l3 3v-3h3V4h-5v7z" opacity=".85"/></svg></span>Company Secial Message</header>
  <blockquote><span class="q">&ldquo;</span> Lorem ipsum dolor amet, conse ctetuer adipiscing elit, sed diam nonu mmy nibh euis mod tincidunt ut laore et dolore ma gna aliquam erat volutpat. Ut wisi enim ad ,  Lorem ipsum dolor amet, conse ctetuer adipiscing elit, sed diam nonummy. <span class="q">&rdquo;</span></blockquote>
</article>

<div class="crest" role="img" aria-label="Company emblem area">
  <svg width="205" height="242" viewBox="0 0 205 242"><circle cx="102" cy="121" r="92" fill="var(--blue)"/></svg>
</div>

<footer class="footer">© 2016 Sentinel Watch Services.&nbsp; All Rights Reserved</footer>

</body>
</html>
```